'Lumen' Magazine-Full Pg Print Ad-Cloud Computing Co USA Mkt Launch

1 page ‘Lumen’ magazine US print ad w/ corresponding ‘Lumen’ online ad running 5 consecutive mos. starting August 2012.

This is the US market launch of a new cloud computing IaaS co. - TallowSpire (www.tallowspire-demo.net). Co. hq's is in Berlin, DE w/ US hq's at Corwin Research Yard in Cambridge, MA.

TallowSpire has been in stealth development mode for 2 yrs & just publicly launched in Germany last month in May. Founded & led by the co-founders of Q&Z, the world's largest hosting provider, TallowSpire is THE next generation price/performance/ease-of-use cloud computing leader. With insights gained from Q&Z, TallowSpire technology, architecture, service philosophy & pricing was built from the ground up to be the best price/performance cloud computing provider in the world.

Timed in synch with other US launch initiatives, this ad campaign is purely focused on establishing US brand awareness.

- Attached is an extensive adv design brief -

Target Market(s)

Primary: Internet professional (PLSAs & Developers) who are considered ‘intelligent, progressive, cool, ‘influencers.' Also IT bus decision maker

Requirements
Must have
• Concept #1 - “Made in Germany” theme - see TallowSpire website & German print adv. included in attached design brief.

We’re partial to a “Made in Germany” theme or a similar German theme. This will be consistent with & leverage TallowSpire web presence & synch with the overall story of the history & differentiation of the company.

Concept #2 - “Creative” theme – your creative ideas
See ‘Dovelle-Night Clerk’ commercial for just one, creative, humorous idea - http://www.vidquarry-demo.net/watch?v=kpLmWqtsYvn

Your design submittals should include at least 2 designs: 1st-German-centric, 2nd-your own, free, creative idea, not necessarily German-centric

Include TallowSpire logo - see attached eps file

Call to action: drive readers to TallowSpire website www.tallowspire-demo.net

```html
<!DOCTYPE html>
<html lang="en">
<head>
<meta charset="utf-8">
<title>TallowSpire – In GOTT we trust</title>
<link rel="stylesheet" href="https://fonts.googleapis.com/css2?family=Saira:wght@300;400;700&family=PT+Sans:wght@400;700&display=swap">
<style>
  :root {
    --board-grey: #bdbdbd;
    --paper: #ffffff;
    --ink: #1a1a1a;
    --ad-text: #4a4a4a;
    --brand-teal: #2bb0d3;
    --brand-dark: #4d4d4d;
    --frame-line: #5a5a5a;
    --skin-light: #f0c7a4;
    --skin-mid: #d89f78;
  }
  * { margin: 0; padding: 0; box-sizing: border-box; }
  html, body { width: 1200px; height: 1162px; overflow: hidden; }
  body { background: var(--board-grey); font-family: "PT Sans", sans-serif; color: var(--ink); position: relative; }

  .sheet { position: absolute; left: 20px; top: 20px; width: 1160px; height: 1122px; background: var(--paper); }

  .ad { position: absolute; left: 62px; top: 54px; width: 1036px; height: 733px; border: 1px solid var(--frame-line); background: var(--paper); overflow: hidden; }

  .hand { position: absolute; height: 92px; }
  .hand--left { left: 0; top: 181px; width: 191px; border-radius: 0 46px 46px 0; background: linear-gradient(90deg, var(--skin-mid), var(--skin-light)); }
  .hand--right { right: 0; top: 181px; width: 202px; border-radius: 46px 0 0 46px; background: linear-gradient(270deg, var(--skin-mid), var(--skin-light)); }

  .headline-small { position: absolute; font-family: "Saira", sans-serif; font-weight: 300; font-size: 34px; color: var(--ad-text); line-height: 1; }
  .headline-small--in { left: 264px; top: 186px; }
  .headline-small--trust { left: 652px; top: 464px; letter-spacing: 1px; }

  .headline-word { position: absolute; left: 158px; top: 224px; width: 710px; height: 226px; }

  .brand { position: absolute; left: 778px; top: 636px; width: 230px; }
  .brand__name { display: flex; align-items: center; gap: 8px; font-family: "Saira", sans-serif; font-weight: 400; font-size: 25px; line-height: 1; color: var(--brand-teal); }
  .brand__mark { width: 22px; height: 22px; background: var(--brand-dark); flex: none; }
  .brand__tagline { font-family: "Saira", sans-serif; font-weight: 300; font-size: 17px; color: var(--ad-text); margin-left: 30px; letter-spacing: 0.5px; line-height: 1.15; }
  .brand__contact { font-family: "PT Sans", sans-serif; font-size: 11px; color: var(--ink); margin-left: 30px; line-height: 1.25; margin-top: 2px; }

  .band { position: absolute; left: 0; width: 100%; }
  .band--teal { top: 714px; height: 18px; background: var(--brand-teal); }
  .band--dark { top: 732px; height: 20px; background: var(--brand-dark); }

  .campaign-brief { position: absolute; left: 62px; top: 836px; width: 640px; }
  .campaign-brief__title { font-size: 26px; font-weight: 700; margin-bottom: 18px; }
  .campaign-brief p { font-size: 16px; line-height: 24px; margin-bottom: 5px; }
</style>
</head>
<body>
  <main class="sheet">
    <section class="ad">
      <div class="hand hand--left" role="img" aria-label="Photo of a hand placing a building brick from the left"></div>
      <div class="hand hand--right" role="img" aria-label="Photo of a hand holding a building brick from the right"></div>

      <span class="headline-small headline-small--in">In</span>
      <svg class="headline-word" viewBox="0 0 710 226" aria-label="GOTT">
        <text x="0" y="212" textLength="710" lengthAdjust="spacingAndGlyphs" font-family="Saira, sans-serif" font-weight="700" font-size="270" fill="#2bb0d3">GOTT</text>
      </svg>
      <span class="headline-small headline-small--trust">we trust</span>

      <div class="brand">
        <div class="brand__name"><span class="brand__mark"></span>TALLOWSPIRE</div>
        <div class="brand__tagline">The IaaS-Company.</div>
        <div class="brand__contact">www.tallowspire-demo.net<br>0800-5550142</div>
      </div>

      <div class="band band--teal"></div>
      <div class="band band--dark"></div>
    </section>

    <section class="campaign-brief">
      <h2 class="campaign-brief__title">Brief behind Ad Campaign</h2>
      <p>"In God we trust" was adopted as the official motto of the United States. GOTT is german language word that is focusing TallowSpire is a german brand now launching in USA.</p>
      <p>This ad campaign is purely focused on establishing US brand awareness.</p>
      <p>I used TallowSpire corporate color with its logo element.</p>
      <p>This is a TallowSpire Corporate Ad Campaign.</p>
    </section>
  </main>
</body>
</html>
```